Modern Design Business Card industrial maintenance company

Business card design for Company named Brookvale Equipment Services

Target Market(s)

Industrial

Industry/Entity Type

Maintenance and repair

Contact Information for Business Card

Place holder for address, office phone, mobile number and email

Requirements
Must have
• Clean modern look
Nice to have
• N/a

```html
<!DOCTYPE html>
<html lang="en">
<head>
<meta charset="utf-8">
<title>Brookvale Equipment Services – Business Card</title>
<link rel="stylesheet" href="https://fonts.googleapis.com/css2?family=Lato:wght@400;700&family=Saira:wght@600&display=swap">
<style>
  :root {
    --backdrop: #939393;
    --card-dark: #1e1e1f;
    --card-light: #ffffff;
    --ink: #111111;
    --silver: #c9c9c9;
    --soft-silver: #bdbdbd;
    --url-white: #f2f2f2;
    --emboss: #2b2b2c;
  }
  html, body {
    margin: 0;
    padding: 0;
    width: 1200px;
    height: 1200px;
    overflow: hidden;
    background: var(--backdrop);
  }
  .canvas {
    position: relative;
    width: 1200px;
    height: 1200px;
  }
  .card {
    position: absolute;
    top: 222px;
    width: 440px;
    height: 795px;
  }
  .card-front {
    left: 107px;
    background: var(--card-dark);
  }
  .card-front svg { display: block; }
  .card-back {
    left: 643px;
    background: var(--card-light);
    font-family: "Lato", sans-serif;
    color: var(--ink);
    text-align: center;
  }
  .brand-mark {
    position: absolute;
    left: 0;
    top: 0;
  }
  .holder-name {
    position: absolute;
    left: 0;
    right: 0;
    top: 386px;
    margin: 0;
    font-family: "Saira", sans-serif;
    font-weight: 600;
    font-size: 31px;
    line-height: 1.2;
  }
  .holder-role {
    position: absolute;
    left: 0;
    right: 0;
    top: 429px;
    margin: 0;
    font-size: 20px;
    letter-spacing: 0.5px;
    line-height: 1.2;
  }
  .divider {
    position: absolute;
    left: 191px;
    top: 466px;
    width: 59px;
    height: 2px;
    background: var(--ink);
  }
  .contact-icons {
    position: absolute;
    left: 0;
    top: 507px;
  }
  .contact-lines {
    position: absolute;
    left: 0;
    right: 0;
    top: 546px;
    margin: 0;
    font-size: 20.5px;
    line-height: 29px;
  }
  .pin-icon {
    position: absolute;
    left: 205px;
    top: 660px;
  }
  .address {
    position: absolute;
    left: 0;
    right: 0;
    top: 695px;
    margin: 0;
    font-size: 20.5px;
    line-height: 29px;
    font-style: normal;
  }
</style>
</head>
<body>
<main class="canvas">

  <section class="card card-front" aria-label="Card front">
    <svg width="440" height="795" viewBox="0 0 440 795">
      <text class="front-name" x="-533" y="221" transform="rotate(-90)"
            font-family="Lato, sans-serif" font-weight="700" font-size="38"
            fill="#c9c9c9" textLength="438" lengthAdjust="spacingAndGlyphs">BROOKVALE</text>
      <text class="front-tagline" x="-533" y="246" transform="rotate(-90)"
            font-family="Lato, sans-serif" font-size="14"
            fill="#bdbdbd" textLength="441" lengthAdjust="spacing">EQUIPMENT SERVICES</text>
      <text class="front-url" x="-514" y="409" transform="rotate(-90)"
            font-family="Lato, sans-serif" font-size="17.5"
            fill="#f2f2f2" textLength="233" lengthAdjust="spacingAndGlyphs">www.brookvale.com.au</text>
      <circle class="front-seal" cx="219" cy="629" r="66" fill="none" stroke="#2b2b2c" stroke-width="4"/>
    </svg>
  </section>

  <section class="card card-back" aria-label="Card back">
    <svg class="brand-mark" width="440" height="340" viewBox="0 0 440 340">
      <circle cx="220" cy="203" r="129" fill="none" stroke="#111111" stroke-width="8"/>
      <text x="220" y="214" text-anchor="middle" font-family="Lato, sans-serif"
            font-weight="700" font-size="34" fill="#111111">Brookvale</text>
    </svg>

    <h1 class="holder-name">Daniel Reyes</h1>
    <p class="holder-role">Founder &amp; CEO</p>
    <div class="divider"></div>

    <svg class="contact-icons" width="440" height="32" viewBox="0 0 440 32" aria-hidden="true">
      <g fill="#111111">
        <circle cx="186" cy="16" r="15"/>
        <circle cx="220" cy="16" r="15"/>
        <circle cx="254" cy="16" r="15"/>
      </g>
      <g fill="#ffffff">
        <path d="M178 13 q8 -6 16 0 v2 h-3 v-2 q-5 -2 -10 0 v2 h-3 z"/>
        <rect x="180" y="15" width="12" height="7" rx="1.5"/>
        <path d="M214 9 l3 -1 l2 4 l-2 2 q1 3 4 5 l2 -2 l4 2 l-1 3 q-9 1 -12 -13 z"/>
        <rect x="246" y="10.5" width="16" height="11" rx="2"/>
      </g>
      <path d="M246.5 11.5 l7.5 6 l7.5 -6" fill="none" stroke="#111111" stroke-width="1.6"/>
    </svg>

    <p class="contact-lines">000 000 0000<br>000 000 0000<br>info@brookvale.com.au</p>

    <svg class="pin-icon" width="30" height="30" viewBox="0 0 30 30" aria-hidden="true">
      <circle cx="15" cy="15" r="15" fill="#111111"/>
      <path d="M15 6 a6 6 0 0 1 6 6 c0 4.5 -6 11 -6 11 s-6 -6.5 -6 -11 a6 6 0 0 1 6 -6 z" fill="#ffffff"/>
      <circle cx="15" cy="12" r="2.3" fill="#111111"/>
    </svg>

    <address class="address">24 Mill Road, Harbourton<br>SA 200C014</address>
  </section>

</main>
</body>
</html>
```